Proofreading business card design needed

I need a business card for a proofreading business based in Kempsey.
It is our business to scour our clients' written word finding and fixing errors.
We: protect people, businesses and organisations from
embarrassment,
safeguard brands and reputations,
save time and money on costly mistakes.
Updates

Hi Everyone,

I need to make a change to my motto - if you have used it.  The last line of my motto needs to say: save you time and money by eliminating costly errors
Sorry about this change, almost at the last minute, but the way it's currently written just didn't put across what I was trying to say.
Thanks
Maren

Target Market(s)

self-publishers, businesses and organisations, research and educational publishers

Industry/Entity Type

Business

Contact Information for Business Card

The Careful Margin Proofing, Maren Colquhoun, Ph: 0491 302 847, Email: maren.check@quillpost.example, www.carefulmarginproofing.example.au, Po Box 5182, West Kempsey, NSW, 2440.

Logo Text

The Careful Margin Proofing

Logo styles of interest
Abstract Logo
Character Logo
Wordmark Logo
Requirements
Nice to have
• Modern take on proofreading or business images: glasses, written word, red pen or pencil, ruler, magnifying glass etc.
Is it possible to have the following text on the card:
'We: protect people, businesses and organisations from
embarrassment,
save time and money on costly mistakes.'
However, I'm totally open to new ideas/concepts.
Would be happy to see some double-sided business card concepts.

```html
<!DOCTYPE html>
<html lang="en">
<head>
<meta charset="utf-8">
<title>The Careful Margin Proofing – Card</title>
<link rel="stylesheet" href="https://fonts.googleapis.com/css2?family=Libre+Baskerville&display=swap">
<style>
  :root {
    --paper: #ffffff;
    --text-muted: #cccccc;
    --accent-red: #c2001b;
  }
  html, body {
    margin: 0;
    padding: 0;
    width: 1200px;
    height: 729px;
    overflow: hidden;
    background: var(--paper);
  }
  .card {
    position: relative;
    width: 1200px;
    height: 729px;
    overflow: hidden;
    background: var(--paper);
  }
  .card__statement {
    position: absolute;
    left: 0;
    top: -14px;
    width: 1205px;
    margin: 0;
    font-family: "Libre Baskerville", Georgia, serif;
    font-size: 41px;
    line-height: 68.5px;
    color: var(--text-muted);
    text-indent: -26px;
    letter-spacing: -0.3px;
  }
  .card__highlight {
    color: var(--accent-red);
  }
</style>
</head>
<body>
  <main class="card">
    <p class="card__statement">
      South Wales, scouring the written word, finding and fixing errors. I run
      <span class="card__highlight">The Careful Margin Proofing</span> and my name is
      <span class="card__highlight">Maren Colquhoun</span>. We protect people,
      businesses and organisations from embarrassment, safeguard brands and
      reputations, save time and money on costly mistakes. You can call me on
      <span class="card__highlight">0491 302 847</span> or you can send me an email via
      <span class="card__highlight">maren.check@quillpost.example</span>. For examples of my work go to
      <span class="card__highlight">carefulmarginproofing.example.au</span>. You can write to me at
      <span class="card__highlight">Po Box 5182, West Kempsey, NSW, 2440</span>. A
      proofreading service based in Kempsey, New South Wales
    </p>
  </main>
</body>
</html>
```